Web Design for Harbor Lane Guild

We need a web design for Harbor Lane Guild. You can see more details about the kind of business that it deals with in this link: http://harborlaneguild.example/. The concept of the site is similar to http://www.kelvora.example/ and we are looking for a homepage design also similar to it.
The top navigation should have:
1) directory
2) articles
3) deals
4) forums
5) log in/register page.
It should also have a video, a slider, map & text as well as a call to action to a "why register page".
As part of the footer it should include:
1) about HLG
2) contact HGL
3) terms & conditions
4) privacy
The color palette for the site will be the UAE flag colors which are red, green, white and black.
Updates
Project Deadline Extended
Reason: We need more designs and options.
Keep sending in more creative designs. thanks.
Industry/Entity Type
Business
Look and feel
Each slider illustrates characteristics of the customer's brand and the style your logo design should communicate.

```html
<!DOCTYPE html>
<html lang="en">
<head>
<meta charset="utf-8">
<title>Harbor Lane Guild</title>
<link href="https://fonts.googleapis.com/css2?family=Cinzel:wght@400;700&family=Open+Sans:ital,wght@0,400;0,600;1,400&display=swap" rel="stylesheet">
<style>
:root{
  --red:#d0121b;
  --red-dark:#a40d14;
  --green:#1f9a4c;
  --green-dark:#137336;
  --accent-green:#3ddc84;
  --ink:#222;
  --text:#555;
  --muted:#8a8a8a;
  --nav:#2f2f2f;
  --paper:#f6f6f6;
  --rule:#cfcfcf;
  --btn:#3a3a3a;
}
*{box-sizing:border-box;margin:0;padding:0}
html,body{width:1200px;height:1170px;overflow:hidden}
body{background:var(--paper);font-family:"Open Sans",Arial,sans-serif;color:var(--text);position:relative}
.abs{position:absolute}

.brand{left:120px;top:40px;display:flex;align-items:center;gap:10px}
.brand-mark{width:28px;height:28px;background:var(--red)}
.brand-name{font-size:26px;font-weight:600;color:var(--red);letter-spacing:.5px}

.contact{right:124px;top:33px;font-size:12px;color:var(--ink)}
.cta-register{left:910px;top:69px;width:170px;height:34px;background:linear-gradient(#25a855,var(--green-dark));border:1px solid #0e5c2a;color:#fff;font-family:"Cinzel",serif;font-weight:700;font-size:12px;display:flex;align-items:center;gap:14px;padding-left:16px;text-decoration:none;letter-spacing:.5px}
.cta-register svg{flex:none}

.main-nav{left:120px;top:122px;width:960px;height:38px;background:linear-gradient(#444,#222);display:flex;align-items:center}
.main-nav a{color:#fff;text-decoration:none;font-family:"Cinzel",serif;font-weight:700;font-size:13px;letter-spacing:.3px;height:38px;display:flex;align-items:center;justify-content:center}
.main-nav .is-active{background:linear-gradient(#e5161f,var(--red-dark));width:106px}
.main-nav .item{width:136px}
.main-nav .item.short{width:118px}
.search{left:836px;top:126px;width:240px;height:30px;background:#fff;border:1px solid #999}
.search svg{position:absolute;right:9px;top:8px}

.slider{left:120px;top:168px;width:960px;height:340px;background:linear-gradient(90deg,#dcdcdc 0%,#f2f2f2 45%,#e6e6e6 75%,#b9bcc2 100%)}
.slide-caption{left:150px;top:276px;width:380px;height:128px;background:rgba(90,90,90,.82);color:#fff;padding:6px 6px 0 7px}
.slide-caption p{font-style:italic;font-size:14.5px;line-height:18px;text-align:justify}
.slide-caption .author{font-style:normal;margin-top:18px;font-size:14.5px}
.slide-caption .author span{color:var(--accent-green)}
.dots{left:552px;top:482px;display:flex;gap:8px}
.dots i{width:13px;height:13px;border-radius:50%;background:#555;border:2px solid #999;display:block}
.dots i:first-child{background:#ddd}

.col{top:530px;width:300px}
.col h2{font-family:"Cinzel",serif;font-weight:400;font-size:16.5px;color:var(--red);letter-spacing:.2px}
.col .photo{margin-top:29px;width:300px;border:1px solid #ddd}
.col p.body{font-size:12px;line-height:18px;text-align:justify;margin-top:6px}
.mission{list-style:none;margin-top:35px}
.mission li{display:flex;gap:14px;font-size:11.5px;line-height:14.5px;text-align:justify;margin-bottom:14px}
.mission li::before{content:"";flex:none;width:13px;height:13px;margin-top:1px;background:var(--green);box-shadow:inset 0 0 0 1px var(--green-dark);clip-path:none}
.mission li .tick{display:none}
.btn{top:821px;height:31px;background:linear-gradient(#4a4a4a,#2a2a2a);border:1px solid #111;color:#fff;font-size:12.5px;font-weight:600;display:flex;align-items:center;justify-content:center;text-decoration:none;width:80px}

.rule{left:120px;width:960px;height:1px;background:var(--rule)}
.partners{left:150px;top:910px;width:900px;height:70px;display:flex;justify-content:space-between;align-items:center}
.partners span{font-size:17px;font-weight:600;color:#8f8f8f}

.foot-brand{left:120px;top:1031px;width:198px;height:66px;background:#fff;display:flex;align-items:center;gap:8px;padding-left:10px}
.foot-brand .brand-mark{width:18px;height:18px}
.foot-brand .brand-name{font-size:15px}
.foot-sep{left:319px;top:1031px;width:2px;height:66px;background:#b9d6c2}
.patron{left:322px;top:1031px;width:316px;height:66px;background:#fff;display:flex;align-items:center;gap:10px;padding-left:18px}
.patron .seal{width:44px;height:44px;border-radius:50%;background:#c9a43a;flex:none}
.patron .txt{text-align:center;font-size:12px;color:var(--ink);line-height:15px;font-weight:600}
.patron .txt b{color:#c8a012;font-size:14px}
.vsep{left:693px;top:1030px;width:1px;height:68px;background:var(--rule)}
.follow{left:740px;top:1051px;font-size:18px;color:#666}
.social{left:859px;top:1045px;display:flex;gap:9px}
.social a{width:29px;height:29px;background:#6b6b6b;display:block}

.bottom-bar{left:0;top:1113px;width:1200px;height:57px;background:#000;color:#888;font-family:Arial,sans-serif;font-size:12px;text-align:center;padding-top:19px}
</style>
</head>
<body>

<header>
  <a class="brand abs" href="#"><span class="brand-mark"></span><span class="brand-name">Harbor Lane Guild</span></a>
  <div class="contact abs">T: +971 (4) 555 0142 | F: +971 (4) 555 0198</div>
  <a class="cta-register abs" href="#">
    <svg width="24" height="22" viewBox="0 0 24 22"><rect x="1" y="4" width="16" height="16" fill="none" stroke="#fff" stroke-width="2"/><path d="M8 14 L20 2 L23 5 L11 17 L7 18 Z" fill="#fff"/></svg>
    WHY REGISTER?
  </a>
  <nav class="main-nav abs">
    <a class="is-active" href="#">HOME</a>
    <a class="item" href="#">DIRECTORY</a>
    <a class="item short" href="#">ARTICLES</a>
    <a class="item short" href="#">DEALS</a>
    <a class="item" href="#">FORUMS</a>
    <a class="item short" href="#">LOG IN</a>
  </nav>
  <div class="search abs"><svg width="13" height="13" viewBox="0 0 13 13"><circle cx="4.5" cy="4.5" r="3.2" fill="none" stroke="#222" stroke-width="1.8"/><path d="M7 7 L12 12" stroke="#222" stroke-width="2.2"/></svg></div>
</header>

<section>
  <div class="slider abs" role="img" aria-label="Photo of business people in conversation at a meeting"></div>
  <div class="slide-caption abs">
    <p>Lorem ipsum dolor sit amet, consectetur adipisicing elit, sed do eiusmod tempor incididunt ut labore et dolore magna aliqua. Ut enim ad minim veniam, quis nostrud exercitation ullamco laboris nisi ut al</p>
    <p class="author"><span>Marco</span>, Lorem ipsum</p>
  </div>
  <div class="dots abs"><i></i><i></i><i></i><i></i><i></i></div>
</section>

<section>
  <div class="col abs" style="left:120px">
    <h2>WELCOME TO HARBOR LANE GUILD</h2>
    <div class="photo" role="img" aria-label="Photo of a smiling businessman in front of his team" style="height:141px;background:linear-gradient(90deg,#5a4a3e,#d8d8d8 45%,#9a9a9a)"></div>
    <p class="body">Lorem ipsum dolor sit amet, consectetur adipisicing elit, sed do eiusmod tempor incididunt ut labore et dolore magna aliqua. Ut enim ad minim veniam, quis nostrud exercitation ullamco laboris nisi ut al</p>
  </div>
  <a class="btn abs" href="#" style="left:120px">Read More</a>

  <div class="col abs" style="left:450px">
    <h2>OUR MISSION</h2>
    <ul class="mission">
      <li>Harbor Lane Guild will allow you to maximize the potential of your Harbor Lane business.</li>
      <li>A business Networking Platform helping Harbor Lane members' source new customers.</li>
      <li>Provide a supportive infrastructure to enable companies to access and engage in unlimited networking opportunities.</li>
      <li>Build mutual business relationships with fellow Harbor Lane companies.</li>
      <li>As a Harbor Lane Guild member, you will have the opportunity to improve business techniques...</li>
    </ul>
  </div>
  <a class="btn abs" href="#" style="left:450px">Read More</a>

  <div class="col abs" style="left:780px">
    <h2>HOW IT WORKS</h2>
    <div class="photo" role="img" aria-label="Video still of colleagues gathered around a laptop, with a play button" style="height:212px;background:linear-gradient(135deg,#6a5a50,#d9d4cc 50%,#8aa8b0);position:relative">
      <svg style="position:absolute;left:98px;top:80px" width="108" height="66" viewBox="0 0 108 66"><rect x="1" y="1" width="106" height="64" rx="6" fill="rgba(255,255,255,.25)" stroke="rgba(255,255,255,.6)"/><path d="M44 14 L70 33 L44 52 Z" fill="rgba(255,255,255,.8)"/></svg>
    </div>
  </div>
  <a class="btn abs" href="#" style="left:780px">See More</a>
</section>

<div class="rule abs" style="top:889px"></div>
<div class="partners abs">
  <span>Corvella</span><span>Pradena</span><span>Ridgeback Grill</span><span>Saltmere Cruises</span><span>Orchard Table</span><span>Brightleaf</span><span>Zesto</span>
</div>
<div class="rule abs" style="top:998px"></div>

<footer>
  <div class="foot-brand abs"><span class="brand-mark"></span><span class="brand-name">Harbor Lane Guild</span></div>
  <div class="foot-sep abs"></div>
  <div class="patron abs"><span class="seal"></span><div class="txt">A<br><b>Sheikh Omar bin Tariq Al Saeed</b><br>Project</div></div>
  <div class="vsep abs"></div>
  <div class="follow abs">Follow us</div>
  <div class="social abs">
    <a href="#" aria-label="Social link 1"></a><a href="#" aria-label="Social link 2"></a><a href="#" aria-label="Social link 3"></a><a href="#" aria-label="Social link 4"></a><a href="#" aria-label="Social link 5"></a><a href="#" aria-label="Feed link"></a>
  </div>
  <div class="bottom-bar abs">© 2013 Harbor Lane Guild | All Rights Reserved</div>
</footer>

</body>
</html>
```